Penwick Insurance Post Card

Specializing in “Towing & Transportation Insurance”
See our website at http://penwickins-example.net/ for ideas on colors fonts etc.

Target Market(s)

Towing Companies

Font styles to use
Serif
Sans Serif

Requirements
Must have
• Specializing in “Towing & Transportation Insurance”
• Welcome to Penwick Insurance:
• 2nd sentence (With our Agency, we work to make ourselves available to your business for when you need us most to keep your business moving forward.)
• 3rd Sentence: (Our customers were in mind when developing our agency and will continue to find new ways to make doing business with us easier.)
• We Offer: Change “Dealers Physical Damage” to “Auto Dealer Liability” & “Garage Liability” to “Garage Repair Liability”
• Our address: 418 5th St NW, Suite B Decatur, AL 35602
• Email Address: PenwickInfo@velmorlink.example

```html
<!DOCTYPE html>
<html lang="en">
<head>
<meta charset="utf-8">
<title>Penwick Insurance Post Card</title>
<link rel="stylesheet" href="https://fonts.googleapis.com/css2?family=Cinzel:wght@400;600&family=Questrial&family=Roboto+Condensed:wght@700&display=swap">
<style>
:root{
  --page:#e8e8e8;
  --navy:#13355f;
  --blue:#275f96;
  --blue-mid:#1f4d80;
  --gold:#c08b22;
  --gold-light:#e9bd52;
  --grey:#d9dade;
  --grey-light:#f3f3f4;
  --ink:#2b2b2b;
  --white:#ffffff;
  --photo-a:#8d8f93;
  --photo-b:#4f5d73;
}
*{box-sizing:border-box;margin:0;padding:0}
html,body{width:689px;height:1200px;overflow:hidden}
body{background:var(--page);position:relative;font-family:"Questrial",sans-serif;color:var(--ink)}
.card{position:absolute;left:45px;width:600px;height:432px;background:var(--white);overflow:hidden;box-shadow:0 3px 10px rgba(0,0,0,.25)}
.card--front{top:110px}
.card--back{top:620px}

/* front */
.front-header{position:absolute;left:0;top:0;width:100%;height:78px;background:linear-gradient(180deg,var(--navy),var(--blue));display:flex;align-items:center;justify-content:center}
.brand{font-family:"Cinzel",serif;font-weight:400;letter-spacing:3px;white-space:nowrap}
.front-header .brand{color:var(--white);font-size:28px}
.tagline-band{position:absolute;left:0;top:78px;width:100%;height:32px;background:linear-gradient(90deg,var(--gold),var(--gold-light) 55%,var(--gold));display:flex;align-items:center;justify-content:center;font-family:"Cinzel",serif;font-weight:600;font-size:16px;color:var(--white);letter-spacing:.3px}
.welcome{position:absolute;left:0;top:110px;width:295px;height:155px;background:linear-gradient(180deg,var(--grey) 0,var(--grey-light) 32%,var(--white) 60%);padding:8px 12px 0}
.welcome h2{font-family:"Cinzel",serif;font-weight:400;text-align:center;color:var(--navy);font-size:19px;line-height:1.1}
.welcome h2 strong{display:block;font-weight:600;font-size:19px}
.welcome p{font-size:9.3px;line-height:1.3;margin-top:9px}
.welcome p + p{margin-top:7px}
.offer{position:absolute;left:0;top:265px;width:295px;height:127px;background:linear-gradient(180deg,var(--blue-mid),var(--navy));padding:0 12px}
.tag{display:inline-block;background:linear-gradient(90deg,var(--gold),var(--gold-light));color:var(--navy);font-family:"Questrial",sans-serif;font-size:12px;padding:2px 12px;letter-spacing:.5px}
.offer .tag{position:absolute;left:102px;top:6px}
.offer-list{position:absolute;top:30px;left:12px;right:8px;display:grid;grid-template-columns:150px 1fr;row-gap:3px;list-style:none;color:var(--white);font-size:9.6px;grid-auto-flow:column;grid-template-rows:repeat(6,auto)}
.offer-list li{display:flex;align-items:center;gap:5px}
.offer-list svg{width:8px;height:8px;flex:none}
.contact{position:absolute;left:0;top:392px;width:295px;height:40px;display:flex;align-items:center;padding:0 10px;gap:9px}
.phone{display:flex;align-items:center;gap:4px;font-family:"Roboto Condensed",sans-serif;font-weight:700;font-size:18px;color:var(--navy)}
.phone svg{width:14px;height:14px}
.divider{width:1px;height:28px;background:var(--navy)}
.links{list-style:none;font-size:8.4px;color:var(--navy);line-height:1.55}
.links li{display:flex;align-items:center;gap:4px}
.links svg{width:9px;height:9px}
.photo{position:absolute;background:linear-gradient(160deg,var(--photo-a),var(--photo-b))}
.photo--main{left:297px;top:112px;width:303px;height:200px}
.photo--ramp{left:297px;top:315px;width:185px;height:117px;background:linear-gradient(160deg,#b9bcc0,#6e7378)}
.photo--hitch{left:485px;top:315px;width:115px;height:117px;background:linear-gradient(160deg,#c9cbce,#7d8085)}

/* back */
.back-brand{position:absolute;left:0;top:12px;width:340px;text-align:center}
.back-brand .brand{color:var(--navy);font-size:24px}
.back-brand .sub{font-size:7px;color:var(--gold);margin-top:3px}
.back-panel{position:absolute;left:0;top:70px;width:345px;height:322px;clip-path:polygon(0 0,345px 0,295px 100%,0 100%)}
.back-panel .photo--truck{left:0;top:0;width:100%;height:154px;background:linear-gradient(180deg,#a9b7c6 0,#8d8679 55%,#b8ad98)}
.about{position:absolute;left:0;top:154px;width:100%;height:168px;background:linear-gradient(180deg,var(--blue-mid),var(--navy));padding:0 12px}
.about .tag{position:absolute;left:100px;top:5px}
.about p{position:absolute;top:34px;left:10px;width:290px;color:var(--white);font-size:8.2px;line-height:1.33;text-align:justify}
.card--back .contact{top:392px}
.address{position:absolute;left:356px;top:16px;font-size:10.5px;line-height:1.35;color:var(--ink)}
.stamp{position:absolute;left:512px;top:22px;width:70px;height:62px;border:1px solid #555}
.address-lines{position:absolute;left:360px;top:245px;width:222px}
.address-lines span{display:block;height:1px;background:#777;margin-bottom:36px}
</style>
</head>
<body>

<section class="card card--front">
  <header class="front-header"><span class="brand">PENWICK INSURANCE</span></header>
  <div class="tagline-band">SPECIALIZING IN TOWING &amp; TRANSPORTATION INSURANCE</div>

  <div class="welcome">
    <h2>WELCOME TO<strong>PENWICK INSURANCE</strong></h2>
    <p>With our Agency, we work to make ourselves available to your business for when you need us most to keep your business moving forward.</p>
    <p>Our customers were in mind when developing our agency and will continue to find new ways to make doing business with us easier.</p>
  </div>

  <div class="offer">
    <span class="tag">WE OFFER</span>
    <ul class="offer-list">
      <li><svg viewBox="0 0 10 10"><circle cx="5" cy="5" r="4.3" fill="none" stroke="#e9bd52" stroke-width="1.2"/><path d="M4 3l2 2-2 2" fill="none" stroke="#e9bd52" stroke-width="1.2"/></svg>Auto Liability</li>
      <li><svg viewBox="0 0 10 10"><circle cx="5" cy="5" r="4.3" fill="none" stroke="#e9bd52" stroke-width="1.2"/><path d="M4 3l2 2-2 2" fill="none" stroke="#e9bd52" stroke-width="1.2"/></svg>General Liability</li>
      <li><svg viewBox="0 0 10 10"><circle cx="5" cy="5" r="4.3" fill="none" stroke="#e9bd52" stroke-width="1.2"/><path d="M4 3l2 2-2 2" fill="none" stroke="#e9bd52" stroke-width="1.2"/></svg>Garage Repair Liability</li>
      <li><svg viewBox="0 0 10 10"><circle cx="5" cy="5" r="4.3" fill="none" stroke="#e9bd52" stroke-width="1.2"/><path d="M4 3l2 2-2 2" fill="none" stroke="#e9bd52" stroke-width="1.2"/></svg>Garagekeepers</li>
      <li><svg viewBox="0 0 10 10"><circle cx="5" cy="5" r="4.3" fill="none" stroke="#e9bd52" stroke-width="1.2"/><path d="M4 3l2 2-2 2" fill="none" stroke="#e9bd52" stroke-width="1.2"/></svg>Auto Dealer Liability</li>
      <li><svg viewBox="0 0 10 10"><circle cx="5" cy="5" r="4.3" fill="none" stroke="#e9bd52" stroke-width="1.2"/><path d="M4 3l2 2-2 2" fill="none" stroke="#e9bd52" stroke-width="1.2"/></svg>OnHook</li>
      <li><svg viewBox="0 0 10 10"><circle cx="5" cy="5" r="4.3" fill="none" stroke="#e9bd52" stroke-width="1.2"/><path d="M4 3l2 2-2 2" fill="none" stroke="#e9bd52" stroke-width="1.2"/></svg>Cargo</li>
      <li><svg viewBox="0 0 10 10"><circle cx="5" cy="5" r="4.3" fill="none" stroke="#e9bd52" stroke-width="1.2"/><path d="M4 3l2 2-2 2" fill="none" stroke="#e9bd52" stroke-width="1.2"/></svg>Property</li>
      <li><svg viewBox="0 0 10 10"><circle cx="5" cy="5" r="4.3" fill="none" stroke="#e9bd52" stroke-width="1.2"/><path d="M4 3l2 2-2 2" fill="none" stroke="#e9bd52" stroke-width="1.2"/></svg>Wrongful Repossession</li>
      <li><svg viewBox="0 0 10 10"><circle cx="5" cy="5" r="4.3" fill="none" stroke="#e9bd52" stroke-width="1.2"/><path d="M4 3l2 2-2 2" fill="none" stroke="#e9bd52" stroke-width="1.2"/></svg>Umbrella/Excess</li>
      <li><svg viewBox="0 0 10 10"><circle cx="5" cy="5" r="4.3" fill="none" stroke="#e9bd52" stroke-width="1.2"/><path d="M4 3l2 2-2 2" fill="none" stroke="#e9bd52" stroke-width="1.2"/></svg>Workers Compensation</li>
    </ul>
  </div>

  <div class="contact">
    <span class="phone"><svg viewBox="0 0 24 24"><path fill="#13355f" d="M6.6 10.8c1.4 2.8 3.8 5.1 6.6 6.6l2.2-2.2c.3-.3.7-.4 1-.2 1.1.4 2.3.6 3.6.6.6 0 1 .4 1 1V20c0 .6-.4 1-1 1C10.6 21 3 13.4 3 4c0-.6.4-1 1-1h3.5c.6 0 1 .4 1 1 0 1.3.2 2.5.6 3.6.1.3 0 .7-.2 1l-2.3 2.2z"/></svg>334 555 0187</span>
    <span class="divider"></span>
    <ul class="links">
      <li><svg viewBox="0 0 10 10"><circle cx="5" cy="5" r="4.3" fill="none" stroke="#13355f"/><path d="M1 5h8M5 1c2 2.5 2 5.5 0 8M5 1c-2 2.5-2 5.5 0 8" fill="none" stroke="#13355f" stroke-width=".7"/></svg>penwickins-example.net</li>
      <li><svg viewBox="0 0 10 10"><circle cx="5" cy="5" r="4.5" fill="#13355f"/><rect x="2.5" y="3.3" width="5" height="3.4" fill="none" stroke="#fff" stroke-width=".7"/><path d="M2.5 3.3L5 5.3l2.5-2" fill="none" stroke="#fff" stroke-width=".7"/></svg>PenwickInfo@velmorlink.example</li>
    </ul>
  </div>

  <div class="photo photo--main" role="img" aria-label="Photo: a damaged blue sedan loaded on a flatbed tow truck in a city street"></div>
  <div class="photo photo--ramp" role="img" aria-label="Photo: a silver car being pulled up the tilted ramp of a flatbed"></div>
  <div class="photo photo--hitch" role="img" aria-label="Photo: close view of a tow truck's rear lift and chains"></div>
</section>

<section class="card card--back">
  <div class="back-brand">
    <span class="brand">PENWICK INSURANCE</span>
    <div class="sub">Specializing in Towing &amp; Transportation Insurance</div>
  </div>

  <div class="back-panel">
    <div class="photo photo--truck" role="img" aria-label="Photo: a white flatbed tow truck carrying an old maroon car in front of desert mountains"></div>
    <div class="about">
      <span class="tag">ABOUT US</span>
      <p>This agency was started with the idea of doing business in such a way that would look &amp; feel different than most agencies. Over time, we found a comfortable fit in the Towing, Transportation, &amp; Automotive industry which led us to committing our full attention to their insurance needs. We have partnered with over 20 companies that offer specialized insurance packages specifically for those types of businesses. We try hard to make each day purposeful and treat each customer as if they were our only one. I would have to say our motto is, “Be friendly to everyone, help all who ask for it, and work each day as if God Himself was handing you the paycheck.”</p>
    </div>
  </div>

  <div class="contact">
    <span class="phone"><svg viewBox="0 0 24 24"><path fill="#13355f" d="M6.6 10.8c1.4 2.8 3.8 5.1 6.6 6.6l2.2-2.2c.3-.3.7-.4 1-.2 1.1.4 2.3.6 3.6.6.6 0 1 .4 1 1V20c0 .6-.4 1-1 1C10.6 21 3 13.4 3 4c0-.6.4-1 1-1h3.5c.6 0 1 .4 1 1 0 1.3.2 2.5.6 3.6.1.3 0 .7-.2 1l-2.3 2.2z"/></svg>334 555 0187</span>
    <span class="divider"></span>
    <ul class="links">
      <li><svg viewBox="0 0 10 10"><circle cx="5" cy="5" r="4.3" fill="none" stroke="#13355f"/><path d="M1 5h8M5 1c2 2.5 2 5.5 0 8M5 1c-2 2.5-2 5.5 0 8" fill="none" stroke="#13355f" stroke-width=".7"/></svg>penwickins-example.net</li>
      <li><svg viewBox="0 0 10 10"><circle cx="5" cy="5" r="4.5" fill="#13355f"/><rect x="2.5" y="3.3" width="5" height="3.4" fill="none" stroke="#fff" stroke-width=".7"/><path d="M2.5 3.3L5 5.3l2.5-2" fill="none" stroke="#fff" stroke-width=".7"/></svg>PenwickInfo@velmorlink.example</li>
    </ul>
  </div>

  <address class="address" style="font-style:normal">418 5th St NW,<br>Suite B Decatur,<br>AL 35602</address>
  <div class="stamp"></div>
  <div class="address-lines"><span></span><span></span><span></span></div>
</section>

</body>
</html>
```